Design a product reviews website

We need a website design and simple logo for the brand Quorvane.com. The website will provide reviews of technology products and services. The brand and website should be approachable but should also be trustworthy and high quality. The deliverable should be designs, specs and assets that I can provide to a development team to build the website.

Target Market(s)

People researching products to buy.

Industry/Entity Type

Product

Logo Text

Quorvane.com

Number of Pages Required

5+ page

Font styles to use
Sans Serif

Colors
0492cd
0355a3
3176b5
33a6d7
85cae6
85abd2
cedeed
cee9f5

Requirements
Must have
• - Designs for the Homepage, Category and Article pages.
• - Designs for web and mobile.
• - Designs details for the engineering team to use for development.
• - I'm open to other colors than the preferences I chose but I'm more likely to like blues, greys and blacks.

```html
<!DOCTYPE html>
<html lang="en">
<head>
<meta charset="utf-8">
<title>Quorvane.com – Product and Services Reviews</title>
<link href="https://fonts.googleapis.com/css2?family=Open+Sans:wght@400;600;700&display=swap" rel="stylesheet">
<style>
:root{
  --blue:#0492cd;
  --navy:#0355a3;
  --mid:#3176b5;
  --sky:#33a6d7;
  --pale:#85cae6;
  --steel:#85abd2;
  --mist:#cedeed;
  --ice:#cee9f5;
  --line:#e3e7ea;
  --white:#ffffff;
  --text:#1d4f86;
}
*{box-sizing:border-box;margin:0;padding:0}
html,body{width:670px;height:1200px;overflow:hidden}
body{font-family:"Open Sans",Arial,sans-serif;background:var(--white);position:relative;color:var(--text)}

.topbar{position:absolute;left:0;top:0;width:670px;height:50px;background:var(--blue);border-bottom:2px solid var(--navy)}
.menu-toggle{position:absolute;left:32px;top:16px;width:17px;height:14px}
.topbar-divider{position:absolute;left:74px;top:0;width:1px;height:48px;background:rgba(255,255,255,.25)}
.brand{position:absolute;left:88px;top:12px;display:flex;align-items:center;gap:7px;color:var(--white);font-weight:700;font-size:17px}
.brand-mark{width:13px;height:13px;background:var(--white);border-radius:2px}
.search{position:absolute;left:334px;top:12px;width:302px;height:24px;border-radius:12px;background:var(--white);overflow:hidden}
.search span{position:absolute;left:11px;top:5px;font-size:7px;color:#666}
.search-btn{position:absolute;right:0;top:0;width:28px;height:24px;background:var(--navy);border-radius:0 12px 12px 0}
.search-btn svg{position:absolute;left:8px;top:6px}

.hero{position:absolute;left:0;top:50px;width:670px;height:194px;background:linear-gradient(100deg,#3c3f45 0%,#5b6470 35%,#2c3038 60%,#4a6b8a 85%,#2b3a4c 100%);text-align:center;color:var(--white)}
.hero-title{position:absolute;left:0;right:0;top:52px;display:flex;justify-content:center;align-items:center;gap:10px;font-size:32px;font-weight:700}
.hero-title .brand-mark{width:26px;height:26px;border-radius:3px}
.hero-tag{position:absolute;left:0;right:0;top:94px;font-size:18px;line-height:22px;font-weight:400}

.sidebar{position:absolute;left:34px;top:274px;width:134px;height:234px;background:var(--ice);padding-top:12px}
.nav-item{height:27px;margin-right:2px;display:flex;align-items:center;gap:6px;padding-left:12px;font-size:8px;font-weight:700;color:var(--navy);border-bottom:1px dashed var(--white)}
.nav-item i{width:6px;height:6px;background:var(--navy);border-radius:1px;display:block}
.nav-item.active{background:var(--blue);color:var(--white);border-right:3px solid var(--navy);border-bottom:none;margin-right:12px}
.nav-item.active i{background:var(--white)}

.section-title{position:absolute;top:270px;font-size:14px;font-weight:700;color:var(--navy)}

.card{position:absolute;border:1px solid var(--line);background:var(--white);padding:10px}
.photo{display:block;width:100%}
.tags{display:flex;gap:4px;margin-top:10px}
.tag{border:1px solid var(--mid);font-size:7px;padding:3px 6px;color:var(--navy)}
.card-title{font-size:11px;font-weight:600;color:var(--navy);margin-top:6px;line-height:14px}
.meta{font-size:7px;color:var(--mid);margin-top:5px;display:flex;gap:6px;align-items:center}
.meta b{display:inline-block;width:5px;height:5px;background:var(--sky);border-radius:1px;margin-right:3px}

.load-more{position:absolute;left:174px;top:1099px;width:308px;height:21px;background:var(--steel);color:var(--white);font-size:7px;font-weight:700;display:flex;align-items:center;justify-content:center;gap:4px}

.footer{position:absolute;left:0;top:1140px;width:670px;height:60px;background:var(--blue);color:var(--white)}
.copyright{position:absolute;left:34px;top:25px;font-size:7px}
.social{position:absolute;right:30px;top:22px;display:flex;gap:4px}
.social span{width:16px;height:16px;border-radius:50%;display:block}
</style>
</head>
<body>

<header class="topbar">
  <svg class="menu-toggle" viewBox="0 0 17 14"><rect width="17" height="2.5" fill="#fff"/><rect y="5.7" width="17" height="2.5" fill="#fff"/><rect y="11.4" width="17" height="2.5" fill="#fff"/></svg>
  <div class="topbar-divider"></div>
  <div class="brand"><span class="brand-mark"></span>Quorvane.com</div>
  <div class="search"><span>Search..</span><div class="search-btn"><svg width="12" height="12" viewBox="0 0 12 12"><circle cx="5" cy="5" r="3.6" fill="none" stroke="#fff" stroke-width="1.6"/><line x1="7.7" y1="7.7" x2="11" y2="11" stroke="#fff" stroke-width="1.8"/></svg></div></div>
</header>

<section class="hero" role="img" aria-label="Blurred photo of a man reviewing charts on a laptop screen">
  <div class="hero-title"><span class="brand-mark"></span>Quorvane.com</div>
  <p class="hero-tag">The Best Product and Services<br>Reviews and Rankings</p>
</section>

<nav class="sidebar">
  <div class="nav-item active"><i></i>HOME</div>
  <div class="nav-item"><i></i>APPLIANCES</div>
  <div class="nav-item"><i></i>COMPUTERS</div>
  <div class="nav-item"><i></i>ELECTRONICS</div>
  <div class="nav-item"><i></i>HOME SECURITY</div>
  <div class="nav-item"><i></i>MOBILE</div>
  <div class="nav-item"><i></i>SMART HOME</div>
  <div class="nav-item"><i></i>SOFTWARE</div>
</nav>

<h2 class="section-title" style="left:180px">NEWS</h2>
<h2 class="section-title" style="left:493px">POPULAR</h2>

<article class="card" style="left:174px;top:296px;width:308px;height:279px">
  <div class="photo" role="img" aria-label="Purple portable speaker on a desk" style="height:194px;background:linear-gradient(120deg,#c9c6c0,#5a4f8a 50%,#22253a)"></div>
  <div class="tags"><span class="tag">Home</span><span class="tag">Speaker</span></div>
  <h3 class="card-title">Vestibulum ante ipsum primis in faucibus orci luctus</h3>
  <div class="meta"><span><b></b>Mara Quell</span>|<span><b></b>Aug 10, 2016</span></div>
</article>

<article class="card" style="left:174px;top:582px;width:147px;height:222px">
  <div class="photo" role="img" aria-label="Smartphone resting on a tablet" style="height:118px;background:linear-gradient(135deg,#2a62b8,#6fa5d8 50%,#2f2f35)"></div>
  <div class="tags"><span class="tag">Mobile</span></div>
  <h3 class="card-title">Vestibulum ante ipsum primis in faucibus</h3>
  <div class="meta"><span><b></b>Mara Quell</span>|<span><b></b>Aug 10, 2016</span></div>
</article>

<article class="card" style="left:336px;top:582px;width:146px;height:222px">
  <div class="photo" role="img" aria-label="Film camera on a white table" style="height:118px;background:linear-gradient(135deg,#e9eef3,#9aa1a8 50%,#e8ecf0)"></div>
  <div class="tags"><span class="tag">Electronic</span></div>
  <h3 class="card-title">Vestibulum ante ipsum primis in faucibus</h3>
  <div class="meta"><span><b></b>Mara Quell</span>|<span><b></b>Aug 10, 2016</span></div>
</article>

<article class="card" style="left:174px;top:811px;width:308px;height:280px">
  <div class="photo" role="img" aria-label="Red toaster on a kitchen counter" style="height:194px;background:linear-gradient(120deg,#b8b2ac,#c02a2a 50%,#8c8580)"></div>
  <div class="tags"><span class="tag">Home Appliances</span></div>
  <h3 class="card-title">Vestibulum ante ipsum primis in faucibus orci luctus</h3>
  <div class="meta"><span><b></b>Mara Quell</span>|<span><b></b>Aug 10, 2016</span></div>
</article>

<div class="load-more"><svg width="6" height="6" viewBox="0 0 6 6"><circle cx="3" cy="3" r="2.2" fill="none" stroke="#fff" stroke-width="1" stroke-dasharray="2 1"/></svg>LOAD MORE</div>

<article class="card" style="left:489px;top:296px;width:147px;height:202px">
  <div class="photo" role="img" aria-label="Bright living room interior" style="height:118px;background:linear-gradient(135deg,#d8d4cf,#f2efea 50%,#b89a78)"></div>
  <div class="tags"><span class="tag">Home</span></div>
  <h3 class="card-title">Vestibulum ante ipsum</h3>
  <div class="meta"><span><b></b>Mara Quell</span>|<span><b></b>Aug 10, 2016</span></div>
</article>

<article class="card" style="left:489px;top:504px;width:147px;height:202px">
  <div class="photo" role="img" aria-label="Black wireless speaker on a wooden desk" style="height:118px;background:linear-gradient(135deg,#9a9a9a,#3a3a3a 50%,#d4d4d4)"></div>
  <div class="tags"><span class="tag">Audio</span></div>
  <h3 class="card-title">Vestibulum ante ipsum</h3>
  <div class="meta"><span><b></b>Mara Quell</span>|<span><b></b>Aug 10, 2016</span></div>
</article>

<article class="card" style="left:489px;top:712px;width:147px;height:202px">
  <div class="photo" role="img" aria-label="Modern kitchen with white cabinets" style="height:118px;background:linear-gradient(160deg,#e8e8e6,#9a9a98 55%,#2b2b2b)"></div>
  <div class="tags"><span class="tag">Home</span></div>
  <h3 class="card-title">Vestibulum ante ipsum</h3>
  <div class="meta"><span><b></b>Mara Quell</span>|<span><b></b>Aug 10, 2016</span></div>
</article>

<article class="card" style="left:489px;top:919px;width:147px;height:201px">
  <div class="photo" role="img" aria-label="Desktop computer monitor and keyboard" style="height:118px;background:linear-gradient(135deg,#c89a6a,#e6eaee 50%,#6a5548)"></div>
  <div class="tags"><span class="tag">Computer</span></div>
  <h3 class="card-title">Vestibulum ante ipsum</h3>
  <div class="meta"><span><b></b>Mara Quell</span>|<span><b></b>Aug 10, 2016</span></div>
</article>

<footer class="footer">
  <p class="copyright">Copyright © 2016. Company Name. All Right Reserved</p>
  <div class="social">
    <span style="background:#3b5a9a"></span>
    <span style="background:#2aa3ef"></span>
    <span style="background:#3d3d3d"></span>
    <span style="background:#cb2027"></span>
    <span style="background:#dd4b39"></span>
    <span style="background:#e02a20"></span>
  </div>
</footer>

</body>
</html>
```